Professional Home Buyer business card needed

I need a pretty straight forward business card designed. We help people that NEED to sell their homes solve problems. We perform all types of Real Estate transactions including flip, wholesale, investment, rental property and multi family. The card will mainly be used to give to prospective Sellers but will also be given to Real Estate Investors as well. It should professional and very easy to read, most clients are older people.

Target Market(s)

Distressed home sellers as well as Real Estate investors

Industry/Entity Type

Real Estate

Contact Information for Business Card

should be a professional layout

Colors
ec1f27
ffffff
000000

Requirements
Must have
• Large logo on back and smaller one on front. should utilize Red, white, and black.
• I am thinking of using a soft touch coating on the card so keep that in mind.
• Contact info should be very easy to read, think older clients.
Nice to have
• I would like to see a design with rounded corners on the card
Should not have
• pictures of homes or other home graphics.

```html
<!DOCTYPE html>
<html lang="en">
<head>
<meta charset="utf-8">
<title>Keystone Home Buyers – Business Card</title>
<link href="https://fonts.googleapis.com/css2?family=Open+Sans:wght@400;600;700&family=Saira:wght@500;700&display=swap" rel="stylesheet">
<style>
  :root{
    --red:#ec1f27;
    --black:#000000;
    --white:#ffffff;
    --ink:#1b1b1b;
    --stage:#3b3b3b;
    --rule:#444444;
  }
  *{box-sizing:border-box;margin:0;padding:0}
  html,body{width:1200px;height:900px;overflow:hidden}
  body{
    background:var(--stage);
    font-family:"Open Sans",Arial,sans-serif;
    color:var(--ink);
    display:flex;flex-direction:column;align-items:center;justify-content:center;gap:36px;
  }
  .card{
    position:relative;width:700px;height:400px;background:var(--white);
    border-radius:34px;overflow:hidden;
  }
  .brand{
    display:flex;align-items:center;gap:14px;
    font-family:"Open Sans",Arial,sans-serif;font-weight:700;color:var(--black);
    letter-spacing:1px;text-transform:uppercase;
  }
  .brand__mark{width:22px;height:22px;background:var(--red);flex:none}

  /* back */
  .card--back .brand{position:absolute;top:92px;left:0;right:0;justify-content:center;font-size:40px}
  .card--back .brand__mark{width:30px;height:30px}
  .services{
    position:absolute;left:70px;right:60px;top:210px;
    display:grid;grid-template-columns:1fr 1fr;gap:10px 30px;list-style:none;font-size:21px;
  }
  .services li{display:flex;align-items:center;gap:10px}
  .services li::before{content:"";width:10px;height:10px;border-radius:50%;background:var(--red);flex:none}
  .card--back .edge-line{position:absolute;left:0;right:0;bottom:26px;height:4px;background:var(--red)}
  .card--back .edge-band{position:absolute;left:0;right:0;bottom:0;height:26px;background:var(--black)}

  /* front */
  .card--front .brand{position:absolute;top:52px;left:0;right:0;justify-content:center;font-size:30px}
  .holder{position:absolute;left:60px;top:230px;width:250px;text-align:right}
  .holder__name{font-family:"Saira",Arial,sans-serif;font-weight:500;font-size:34px;color:var(--red);letter-spacing:.5px;line-height:1.1}
  .holder__title{font-size:20px;margin-top:2px}
  .divider{position:absolute;left:340px;top:150px;width:2px;height:150px;background:var(--rule)}
  .contact{position:absolute;left:368px;top:145px;list-style:none;font-size:19px;line-height:1.45}
  .contact li{display:flex;align-items:center;gap:10px}
  .contact svg{width:15px;height:15px;fill:var(--red);flex:none}
  .contact .address{padding-left:0}
  .card--front .edge-line{position:absolute;left:0;right:0;bottom:30px;height:4px;background:var(--black)}
  .card--front .edge-band{position:absolute;left:0;right:0;bottom:0;height:30px;background:var(--red)}
</style>
</head>
<body>
  <section class="card card--back">
    <div class="brand"><span class="brand__mark"></span>Keystone Home Buyers</div>
    <ul class="services">
      <li>Real Estate transactions including flip</li>
      <li>Wholesale</li>
      <li>Investment</li>
      <li>Rental property and multi family</li>
    </ul>
    <div class="edge-line"></div>
    <div class="edge-band"></div>
  </section>

  <section class="card card--front">
    <div class="brand"><span class="brand__mark"></span>Keystone Home Buyers</div>
    <div class="holder">
      <p class="holder__name">DANIEL HARLOW</p>
      <p class="holder__title">Founder &amp; CEO</p>
    </div>
    <div class="divider"></div>
    <ul class="contact">
      <li class="address">512 Ridge Park Ave., Suite 2</li>
      <li class="address">Fairview, NY 12045</li>
      <li><svg viewBox="0 0 24 24"><path d="M6.6 10.8a15 15 0 0 0 6.6 6.6l2.2-2.2a1 1 0 0 1 1-.25 11.4 11.4 0 0 0 3.6.57 1 1 0 0 1 1 1V20a1 1 0 0 1-1 1A17 17 0 0 1 3 4a1 1 0 0 1 1-1h3.5a1 1 0 0 1 1 1c0 1.25.2 2.45.57 3.57a1 1 0 0 1-.25 1z"/></svg>000-000-0000</li>
      <li><svg viewBox="0 0 24 24"><path d="M7 3h10v5H7zM4 9h16a2 2 0 0 1 2 2v6h-4v4H6v-4H2v-6a2 2 0 0 1 2-2zm4 7v3h8v-3z"/></svg>999-999-9999</li>
      <li><svg viewBox="0 0 24 24"><path d="M2 5h20v14H2zm2 2v.5l8 5 8-5V7z"/></svg>info@keystonebuyers.com</li>
      <li><svg viewBox="0 0 24 24"><path d="M12 2a10 10 0 1 0 0 20 10 10 0 0 0 0-20zm0 2c.9 1.2 1.6 3 1.9 5h-3.8c.3-2 1-3.8 1.9-5zM4.3 13a8 8 0 0 1 0-2h3.8a17 17 0 0 0 0 2zm1 2h3.1c.3 1.5.8 2.8 1.4 3.8A8 8 0 0 1 5.3 15zM12 20c-.9-1.2-1.6-3-1.9-5h3.8c-.3 2-1 3.8-1.9 5zm2.2-7H9.8a15 15 0 0 1 0-2h4.4a15 15 0 0 1 0 2zm0 5.8c.6-1 1.1-2.3 1.4-3.8h3.1a8 8 0 0 1-4.5 3.8zM15.9 13a17 17 0 0 0 0-2h3.8a8 8 0 0 1 0 2z"/></svg>www.keystonebuyers.com</li>
    </ul>
    <div class="edge-line"></div>
    <div class="edge-band"></div>
  </section>
</body>
</html>
```